Letter Head, for use on daily correspondence with other companies

Hi

I want a professional Letter head, That my company can use to corresponded with other companies we do business with on a daily basis.

I want this done as soon as possible as this is peak session for us.

I have attached the company logo so please be creative and professional.
Kind regards

Osric

Target Market(s)

All Audience searching for tickets, people in the entertainment world

Industry/Entity Type

Entertainment Industry

Font styles to use
Serif
Sans Serif
Decorative
Script

Requirements
Must have
• Very professional image.
• I will know want i want when i see it
• so please do your utmost in your professional standards
• Address of the company 47 marlow lane, telephone number 0207 581 2937
• Vat number: 486 2917 58.
• This letter head my be able to acomodate usage for directors & CEO as well as managers and employess
Nice to have
• A great professional image
Should not have
• Be creative please

```html
<!DOCTYPE html>
<html lang="en">
<head>
<meta charset="utf-8">
<title>Stagepass Letterhead</title>
<link rel="stylesheet" href="https://fonts.googleapis.com/css2?family=Carlito:wght@400;700&display=swap">
<style>
:root{
  --backdrop:#48494e;
  --paper:#f7f7f7;
  --ink:#111111;
  --brand:#cc2200;
  --brand-text:#ffffff;
}
*{margin:0;padding:0;box-sizing:border-box}
html,body{width:1200px;height:1000px;overflow:hidden}
body{background:var(--backdrop);font-family:"Carlito",Calibri,Arial,sans-serif;position:relative}
.letterhead{position:absolute;left:352px;top:113px;width:501px;height:708px;background:var(--paper);color:var(--ink);font-size:11px;line-height:14px}
.block{position:absolute;left:46px;width:420px}
.date{top:80px}
.recipient{top:108px}
.salutation{top:177px}
.body-copy{top:205px}
.body-copy p{margin-bottom:14px}
.closing{top:483px}
.signatory{top:524px}
.brand-tile{position:absolute;left:407px;top:511px;width:94px;height:65px;background:var(--brand);display:flex;align-items:center;justify-content:center}
.brand-name{color:var(--brand-text);font-weight:700;font-size:18px;letter-spacing:.2px}
.brand-rule{position:absolute;left:407px;top:576px;width:94px;height:2px;background:var(--brand)}
.contact{position:absolute;left:407px;top:579px;list-style:none;color:var(--brand);font-size:8px;font-weight:700;line-height:9px}
.contact li{display:flex;align-items:center}
.contact .icon{width:10px;display:inline-flex;justify-content:center;margin-right:1px}
.contact .vat-mark{font-size:5px;font-weight:700}
</style>
</head>
<body>
<main class="letterhead">
  <p class="block date">August 28, 2011</p>
  <address class="block recipient" style="font-style:normal">First Last Name<br>Street Address<br>City, State 00000</address>
  <p class="block salutation">Dear :</p>
  <div class="block body-copy">
    <p>Lorem ipsum dolor sit amet, consectetur adipiscing elit. Aenean ut ipsum eget massa hendrerit vestibulum vel in velit. Donec pretium neque velit.</p>
    <p>Aliquam porta lectus nec mauris ornare venenatis. Vivamus non est turpis, et cursus sem. Mauris vehicula erat in diam auctor at bibendum nisl lacinia. Morbi imperdiet neque vehicula nunc convallis gravida. Vestibulum iaculis pretium placerat.</p>
    <p>Integer consequat, est sit amet facilisis eleifend, nibh nibh varius orci, eget dapibus arcu dui non purus. Pellentesque in magna mauris. Duis enim sapien, dictum vitae condimentum a, pulvinar vel lacus. Mauris et nibh. Vestibulum vitae nulla at metus elementum porta sit amet interdum elit. Nulla sollicitudin neque eu nulla volutpat congue.</p>
    <p>Etiam pellentesque, velit id dapibus fermentum, turpis sapien ornare dui, ac tincidunt ligula odio congue purus. Nunc sed ante dui, in porta lectus. Cras nec sem lorem. In hac habitasse platea dictumst. Maecenas id diam quis dui porta tristique. Sed id egestas felis. Donec ullamcorper mattis posuere. Phasellus fermentum eleifend tortor vel dapibus. Vestibulum ante ipsum.</p>
  </div>
  <p class="block closing">Sincerely,</p>
  <p class="block signatory">John Doe</p>

  <div class="brand-tile"><span class="brand-name">Stagepass</span></div>
  <div class="brand-rule"></div>
  <ul class="contact">
    <li><span class="icon"><svg width="5" height="7" viewBox="0 0 10 14"><path d="M5 0a5 5 0 0 0-5 5c0 4 5 9 5 9s5-5 5-9a5 5 0 0 0-5-5zm0 7a2 2 0 1 1 0-4 2 2 0 0 1 0 4z" fill="currentColor"/></svg></span>47 Marlow Lane</li>
    <li><span class="icon"><svg width="6" height="6" viewBox="0 0 12 12"><path d="M2.5 0l2 3-1.3 1.3a7 7 0 0 0 4.5 4.5L9 7.5l3 2-1.5 2.2C5 11.5.5 7 .3 1.5z" fill="currentColor"/></svg></span>0207 581 2937</li>
    <li><span class="icon vat-mark">VAT</span>486 2917 58</li>
  </ul>
</main>
</body>
</html>
```